Waterproofing Construction company needs letterhead

I need a letterhead design for a commercial waterproofing construction company. We would like to see designs that are contemporary, clean, sleek and use our logo. Our current design is dated. I would also like a cover page (see example) that goes with our letterhead. I would like for the footer to have our address, website, and phone number

Target Market(s)

Customers, potential customers.

Font styles to use
Sans Serif

Requirements
Must have
• logo, website, address, phone numbers, only our colors, tahoma font
• PMS: 295C PMS: 2995C
• CMYK: 100/84/36/39 CMYK: 80/12/1/0
• RGB: 16/44/82 RGB: 0/167/224
• HEX#: #102C52 HEX#: #00A7E0
• Black & White: 100% Black & White: 32%
• Gray Scale: 90% Gray Scale: 32%
Nice to have
• Our "icon" logo attached would be nice somewhere on the page.

```html
<!DOCTYPE html>
<html lang="en">
<head>
<meta charset="utf-8">
<title>KORVA Letterhead</title>
<link rel="stylesheet" href="https://fonts.googleapis.com/css2?family=Jost:wght@200;400;600;700;800&family=Noto+Sans:wght@400;700&display=swap">
<style>
  :root {
    --navy: #102C52;
    --sky: #00A7E0;
    --headline: #1BA4DF;
    --body: #8A93A3;
    --grey-dark: #555A60;
    --grey-mid: #8C9096;
    --link-blue: #0B5F9E;
    --sig-fill: #EEF1F5;
    --paper: #FFFFFF;
  }
  * { margin: 0; padding: 0; box-sizing: border-box; }
  html, body { width: 849px; height: 1200px; overflow: hidden; background: var(--paper); }
  .letterhead { position: relative; width: 849px; height: 1200px; overflow: hidden; background: var(--paper); }

  .brand-name {
    position: absolute; left: 100px; top: 96px;
    font-family: "Jost", sans-serif; font-weight: 800;
    font-size: 76px; line-height: 1; letter-spacing: -1px;
    color: var(--navy);
  }
  .date {
    position: absolute; right: 125px; top: 252px;
    font-family: "Noto Sans", sans-serif; font-size: 16px; color: #111;
  }
  .accent-dot {
    position: absolute; left: 437px; top: 282px;
    width: 12px; height: 12px; border-radius: 50%;
    background: #DDEFF8;
  }
  .headline {
    position: absolute; left: 99px; top: 313px;
    font-family: "Jost", sans-serif; font-weight: 200;
    font-size: 57px; line-height: 1; color: var(--headline);
  }
  .letter-body {
    position: absolute; left: 102px; top: 392px; width: 650px;
    font-family: "Jost", sans-serif; font-size: 17px; letter-spacing: 0.15px;
    line-height: 22.4px; color: var(--body);
  }
  .letter-body p + p { margin-top: 22.4px; }

  .signature {
    position: absolute; left: 530px; top: 748px;
    width: 188px; height: 92px; border-radius: 6px;
    background: var(--sig-fill);
  }
  .sign-off {
    position: absolute; right: 112px; top: 842px; text-align: right;
    font-family: "Jost", sans-serif; font-size: 16px; line-height: 21px;
  }
  .sign-off .role { font-weight: 700; color: var(--grey-dark); }
  .sign-off .tagline { color: var(--link-blue); }
  .sign-off .site { color: var(--grey-mid); font-size: 15px; }

  .region-band {
    position: absolute; left: 33px; right: 0; top: 1027px; height: 30px;
    background: var(--sky); border-radius: 15px 0 0 15px;
    font-family: "Noto Sans", sans-serif; font-weight: 700;
    font-size: 14.4px; letter-spacing: 0.6px; color: #fff;
    text-align: right; padding-right: 103px; line-height: 30px;
  }
  .contact-rail {
    position: absolute; left: 102px; top: 1061px; width: 22px; height: 150px;
    background: var(--navy); border-radius: 11px 11px 0 0;
  }
  .contact-icon { position: absolute; left: 104px; width: 18px; height: 18px; }
  .contact-list {
    position: absolute; left: 135px; top: 1065px; list-style: none;
    font-family: "Noto Sans", sans-serif; font-size: 14px; color: var(--navy);
  }
  .contact-list li { height: 31px; line-height: 22px; }
  .contact-list b { font-weight: 700; }
</style>
</head>
<body>
<main class="letterhead">
  <div class="brand-name">KORVA</div>

  <div class="date">Date</div>
  <span class="accent-dot"></span>

  <h1 class="headline">HEADLINE</h1>

  <section class="letter-body">
    <p>Lorem ipsum dolor sit amet, consectetur adipiscing elit. Fusce dignissim pretium consectetur. Curabitur tempor posuere massa in varius. Pellentesque viverra nibh eu vehicula mattis. Nullam porta facilisis justo, a feugiat dolor sodales sed. Vestibulum neque nisi, elementum tincidunt metus sit amet, egestas bibendum enim. Aenean a blandit elit, vel rutrum mi. Nunc dapibus turpis sed massa aliquet tincidunt.</p>
    <p>Pellentesque id neque ligula. Nullam posuere, ligula a mattis posuere, lacus nisl adipiscing nunc, eu congue justo est ut diam. Nam quam nibh, dignissim non consequat in, semper eget purus. Nulla arcu sapien, viverra vitae metus tempor, congue ornare diam.</p>
    <p>Pellentesque vel nibh tempus, ullamcorper tortor sed, bibendum augue. Phasellus sollicitudin justo et quam aliquam sollicitudin. Sed eget nibh mollis, mattis sem et, viverra nulla.</p>
  </section>

  <div class="signature" role="img" aria-label="Director's handwritten signature"></div>

  <div class="sign-off">
    <div class="role">Director</div>
    <div class="tagline">Pellentesque id neque ligula. Nullam posuere</div>
    <div class="site">www.companyname.com</div>
  </div>

  <footer>
    <div class="region-band">Eastern Region &nbsp;|&nbsp; Central Region &nbsp;|&nbsp; Coastal Region</div>
    <div class="contact-rail"></div>

    <svg class="contact-icon" style="top:1067px" viewBox="0 0 18 18" aria-hidden="true">
      <circle cx="9" cy="9" r="7" fill="none" stroke="#fff" stroke-width="1.4"/>
      <ellipse cx="9" cy="9" rx="3" ry="7" fill="none" stroke="#fff" stroke-width="1.1"/>
      <line x1="2" y1="9" x2="16" y2="9" stroke="#fff" stroke-width="1.1"/>
    </svg>
    <svg class="contact-icon" style="top:1097px" viewBox="0 0 18 18" aria-hidden="true">
      <path d="M9 1.5a5 5 0 0 0-5 5c0 4 5 10 5 10s5-6 5-10a5 5 0 0 0-5-5z" fill="#fff"/>
      <circle cx="9" cy="6.5" r="1.9" fill="#102C52"/>
    </svg>
    <svg class="contact-icon" style="top:1128px" viewBox="0 0 18 18" aria-hidden="true">
      <path d="M4 2l3 3-1.6 2a9 9 0 0 0 5.6 5.6L13 11l3 3-2 2.2C8 15.5 2.5 10 1.8 4z" fill="#fff"/>
    </svg>

    <ul class="contact-list">
      <li>www.korvaseal.net</li>
      <li>PO Box 417, Linden Falls 40190</li>
      <li><b>O</b>: (800) 555-0172 | <b>F</b>: (800) 555-0186</li>
    </ul>
  </footer>
</main>
</body>
</html>
```